Vantrelo App Homepage Design making customers feel in control of their spend

Hi,
We need a App Homepage design with a UI similar to the attached mock up on an Quorix 4. The app is intended to put customers in control of their usage and spend on their fixed phone, broadband, mobile, gas and electricity.

Please fee free to propose improvements to the background images, icons, colours, etc.

Any questions please let me know.

Thanks
Bertram

Target Market(s)

Consumer customers

Industry/Entity Type

Internet

Font styles to use
Sans Serif

Colors
3276b5
0255a3
85acd3
cfdeed
ffffff

Requirements
Must have
• Content in line with the guidelines in the attached mock up

```html
<!DOCTYPE html>
<html lang="en">
<head>
<meta charset="utf-8">
<title>Vantrelo App Home</title>
<link rel="stylesheet" href="https://fonts.googleapis.com/css2?family=Roboto:wght@300;400;500;700&display=swap">
<style>
  :root {
    --brand-blue: #0b70d2;
    --sky-band: #7cb9ef;
    --white: #ffffff;
    --ring-grey: #8c8c8c;
    --seg-mobile: #ef5b5b;
    --seg-broadband: #f6891f;
    --seg-phone: #95d12a;
    --seg-energy: #17a9f0;
    --seg-gas: #5b2d84;
    --seg-account: #d5001b;
  }
  * { margin: 0; padding: 0; box-sizing: border-box; }
  html, body { width: 675px; height: 1200px; overflow: hidden; background: var(--white); }
  body { font-family: "Roboto", sans-serif; position: relative; color: var(--white); }
  .app-header {
    position: absolute; left: 0; top: 0; width: 675px; height: 104px;
    background: var(--brand-blue);
  }
  .brand-mark {
    position: absolute; left: 28px; top: 30px; width: 44px; height: 44px;
    border-radius: 50%; background: var(--sky-band);
  }
  .brand-name {
    position: absolute; left: 99px; top: 30px;
    font-size: 38px; font-weight: 500; line-height: 44px;
  }
  .menu-toggle { position: absolute; left: 588px; top: 28px; width: 58px; height: 48px; }
  .menu-toggle span {
    position: absolute; left: 0; width: 58px; height: 3px; background: var(--white);
  }
  .menu-toggle span:nth-child(1) { top: 2px; }
  .menu-toggle span:nth-child(2) { top: 23px; }
  .menu-toggle span:nth-child(3) { top: 44px; }
  .greeting {
    position: absolute; left: 0; top: 104px; width: 675px; height: 189px;
    background: var(--sky-band); text-align: center;
  }
  .greeting-title { margin-top: 46px; font-size: 43px; font-weight: 300; line-height: 52px; }
  .greeting-sub { font-size: 33px; font-weight: 300; line-height: 40px; }
  .service-wheel { position: absolute; left: 0; top: 293px; }
  .wheel-label {
    font-family: "Roboto", sans-serif; font-size: 28px; font-weight: 400;
    fill: var(--white); text-anchor: middle; dominant-baseline: central;
  }
  .wheel-icon { fill: none; stroke: var(--white); stroke-width: 2.4; stroke-linecap: round; stroke-linejoin: round; }
  .account-summary {
    position: absolute; left: 0; top: 1096px; width: 675px; height: 104px;
    background: var(--sky-band); text-align: center;
    font-size: 30px; font-weight: 300; line-height: 40px; padding-top: 12px;
  }
</style>
</head>
<body>
  <header class="app-header">
    <div class="brand-mark"></div>
    <div class="brand-name">Vantrelo</div>
    <div class="menu-toggle" aria-label="Menu"><span></span><span></span><span></span></div>
  </header>

  <section class="greeting">
    <h1 class="greeting-title">Good Morning Marta</h1>
    <p class="greeting-sub">Welcome to Vantrelo</p>
  </section>

  <svg class="service-wheel" width="675" height="803" viewBox="0 293 675 803" aria-label="Services wheel">
    <defs>
      <path id="wheel-segment" d="M412.7 514.4 L508.4 459.9 A195 195 0 0 1 508.4 646.1 L412.7 591.6 A85 85 0 0 0 412.7 514.4 Z"/>
    </defs>
    <use href="#wheel-segment" fill="var(--seg-mobile)" transform="rotate(-113 337 553)"/>
    <use href="#wheel-segment" fill="var(--seg-broadband)" transform="rotate(-53 337 553)"/>
    <use href="#wheel-segment" fill="var(--seg-phone)" transform="rotate(7 337 553)"/>
    <use href="#wheel-segment" fill="var(--seg-energy)" transform="rotate(67 337 553)"/>
    <use href="#wheel-segment" fill="var(--seg-gas)" transform="rotate(127 337 553)"/>
    <use href="#wheel-segment" fill="var(--seg-account)" transform="rotate(187 337 553)"/>

    <text class="wheel-label" x="335" y="407">01</text>
    <text class="wheel-label" x="432" y="484">02</text>
    <text class="wheel-label" x="464" y="624">03</text>
    <text class="wheel-label" x="353" y="690">04</text>
    <text class="wheel-label" x="263" y="689">05</text>
    <text class="wheel-label" x="207" y="486">06</text>

    <g class="wheel-icon" transform="translate(274 427)">
      <rect x="-10" y="-21" width="20" height="42" rx="3"/>
      <line x1="-10" y1="-15" x2="10" y2="-15"/>
      <line x1="-10" y1="13" x2="10" y2="13"/>
      <path d="M-18 -7 q-4 7 0 14 M18 -7 q4 7 0 14"/>
    </g>
    <g class="wheel-icon" transform="translate(419 428)">
      <circle r="24"/>
      <ellipse rx="11" ry="24"/>
      <line x1="-24" y1="0" x2="24" y2="0"/>
      <path d="M-20 -13 h40 M-20 13 h40"/>
    </g>
    <g class="wheel-icon" transform="translate(482 563)">
      <path d="M-18 -20 l8 -6 l9 13 l-6 5 q3 9 13 17 l6 -5 l12 10 l-6 8 q-16 2 -30 -14 q-12 -14 -6 -28 Z"/>
    </g>
    <g class="wheel-icon" transform="translate(401 677)">
      <path d="M-8 14 q-12 -10 -6 -22 q8 -12 22 -6 q12 8 4 22 q-3 4 -4 6 h-12 Z"/>
      <line x1="-6" y1="20" x2="6" y2="20"/>
      <path d="M-20 -18 l-5 -5 M0 -26 v-7 M20 -18 l5 -5 M-28 0 h-7 M28 0 h7"/>
    </g>

    <circle cx="601" cy="367" r="45" fill="var(--brand-blue)"/>
    <g class="wheel-icon">
      <path d="M578 376 v-12 q0 -22 23 -22 q8 0 14 4"/>
      <rect x="574" y="364" width="8" height="16" rx="3"/>
      <path d="M582 384 q4 10 16 10"/>
      <circle cx="614" cy="360" r="12"/>
    </g>
    <text x="614" y="364" text-anchor="middle" font-family="Roboto, sans-serif" font-size="11" font-weight="700" fill="var(--white)">24</text>

    <circle cx="72" cy="862" r="35" fill="none" stroke="var(--ring-grey)" stroke-width="1.5"/>
  </svg>

  <footer class="account-summary">
    <p>Last Bill: €75.76 paid on Sept. 12, 2016</p>
    <p>Allowance renews in 18 days</p>
  </footer>
</body>
</html>
```